Bref créative
Fjellbrinken Tannregulering Stationery
Orthodontic Clinic
Professional
Fjellbrinken Tannregulering
Kjeveortoped Stian Haugvik
Myrbakkvegen 128
Postboks 71 Kvernvika
5912 BERGEN
post@smilbrink.no
www.smilbrink.no
Telefon 55 83 17 62

```html
<!DOCTYPE html>
<html lang="nb">
<head>
<meta charset="utf-8">
<title>Fjellbrinken Tannregulering – Stationery</title>
<link rel="stylesheet" href="https://fonts.googleapis.com/css2?family=Open+Sans:wght@400;600;700&display=swap">
<style>
:root{
  --blue:#1e86c8;
  --blue-light:#6fb6e4;
  --green:#6cb33f;
  --ink:#4a4a4a;
  --muted:#8a8a8a;
  --rule:#c9c9c9;
  --paper:#ffffff;
  --stage:#e9e9e9;
}
*{box-sizing:border-box;margin:0;padding:0}
html,body{width:1200px;height:514px;overflow:hidden}
body{background:var(--stage);font-family:"Open Sans",Arial,sans-serif;color:var(--ink);position:relative}
.sheet{position:absolute;background:var(--paper);box-shadow:0 2px 6px rgba(0,0,0,.18);overflow:hidden}
.brand{display:flex;align-items:center;gap:6px;position:absolute}
.brand-dot{width:22px;height:22px;border-radius:50%;background:var(--blue);flex:none}
.brand-name{font-weight:700;color:var(--blue);font-size:9px;line-height:1.1;text-transform:uppercase;letter-spacing:.2px;width:96px}
.brand-tag{font-size:5px;color:var(--muted);margin-top:2px;text-transform:none;font-weight:400}
.header-rule{position:absolute;left:24px;right:24px;height:1px;background:var(--blue-light)}
.swoosh{position:absolute;left:0;bottom:0}
.footer-address{position:absolute;font-size:4.6px;line-height:1.45;color:var(--muted)}
.web-bar{position:absolute;right:0;background:var(--green);color:#fff;font-size:6px;font-weight:600;padding:2px 8px 2px 12px}
/* letterhead */
.letterhead{left:31px;top:24px;width:336px;height:416px}
/* fax */
.fax{left:413px;top:24px;width:336px;height:416px}
.fax-title{position:absolute;left:26px;top:78px;font-size:20px;font-weight:400;color:var(--ink)}
.fax-fields{position:absolute;left:26px;top:112px;width:284px;display:grid;grid-template-columns:1fr 1fr;column-gap:24px;row-gap:9px}
.fax-field{font-size:5px;color:var(--muted);border-bottom:1px solid var(--rule);padding-bottom:3px}
.fax-divider{position:absolute;left:26px;width:284px;height:1px;background:var(--muted)}
.fax-options{position:absolute;left:26px;top:204px;width:284px;display:flex;justify-content:space-between}
.fax-option{font-size:5px;color:var(--muted);display:flex;align-items:center;gap:3px}
.fax-option::before{content:"";width:6px;height:6px;border:1px solid var(--muted)}
/* cards */
.card{width:182px;height:96px;top:29px}
.card-front{left:785px}
.card-back{left:991px}
.card-person{position:absolute;right:10px;top:10px;font-size:5.5px;color:var(--ink);text-align:right;line-height:1.4}
.card-person strong{color:var(--blue);font-size:6px}
/* envelope */
.envelope-back{left:792px;top:158px;width:384px;height:183px}
.recipient-lines{position:absolute;left:232px;top:36px;width:130px}
.recipient-lines span{display:block;height:1px;background:var(--rule);margin-bottom:16px}
.envelope-flap{left:792px;top:360px;width:384px;height:125px}
.flap-mark{position:absolute;left:180px;top:38px;width:24px;height:24px;border-radius:50%;background:var(--paper)}
</style>
</head>
<body>

<!-- Letterhead -->
<section class="sheet letterhead">
  <div class="brand" style="left:24px;top:18px">
    <span class="brand-dot"></span>
    <div class="brand-name">Fjellbrinken Tannregulering<div class="brand-tag">Kjeveortoped Stian Haugvik</div></div>
  </div>
  <div class="header-rule" style="top:56px"></div>
  <svg class="swoosh" width="120" height="70" viewBox="0 0 120 70" aria-hidden="true">
    <path d="M0 10 C10 50 50 66 120 70 L0 70 Z" fill="var(--blue)"/>
    <path d="M0 0 C8 40 40 60 100 68 L0 62 Z" fill="var(--blue-light)" opacity=".55"/>
  </svg>
  <div class="footer-address" style="left:70px;bottom:18px">Myrbakkvegen 128 · Postboks 71 Kvernvika<br>5912 BERGEN<br>Telefon 55 83 17 62 · post@smilbrink.no</div>
  <div class="web-bar" style="bottom:14px">www.smilbrink.no</div>
</section>

<!-- Fax -->
<section class="sheet fax">
  <div class="brand" style="left:24px;top:18px">
    <span class="brand-dot"></span>
    <div class="brand-name">Fjellbrinken Tannregulering<div class="brand-tag">Kjeveortoped Stian Haugvik</div></div>
  </div>
  <h1 class="fax-title">FAX</h1>
  <div class="fax-fields">
    <div class="fax-field">To:</div><div class="fax-field">From:</div>
    <div class="fax-field">Fax:</div><div class="fax-field">Pages:</div>
    <div class="fax-field">Phone:</div><div class="fax-field">Date:</div>
    <div class="fax-field">Re:</div><div class="fax-field">CC:</div>
  </div>
  <div class="fax-divider" style="top:194px"></div>
  <div class="fax-options">
    <span class="fax-option">Urgent</span>
    <span class="fax-option">For Review</span>
    <span class="fax-option">Please Comment</span>
    <span class="fax-option">Please Reply</span>
    <span class="fax-option">Please Recycle</span>
  </div>
  <svg class="swoosh" width="120" height="70" viewBox="0 0 120 70" aria-hidden="true">
    <path d="M0 10 C10 50 50 66 120 70 L0 70 Z" fill="var(--blue)"/>
    <path d="M0 0 C8 40 40 60 100 68 L0 62 Z" fill="var(--blue-light)" opacity=".55"/>
  </svg>
  <div class="footer-address" style="left:70px;bottom:18px">Myrbakkvegen 128 · Postboks 71 Kvernvika<br>5912 BERGEN<br>Telefon 55 83 17 62 · post@smilbrink.no</div>
  <div class="web-bar" style="bottom:14px">www.smilbrink.no</div>
</section>

<!-- Business card, front -->
<section class="sheet card card-front">
  <svg style="position:absolute;left:0;top:0" width="40" height="96" viewBox="0 0 40 96" aria-hidden="true">
    <path d="M0 0 L14 0 C4 30 4 66 22 96 L0 96 Z" fill="var(--blue)"/>
  </svg>
  <div class="brand" style="left:26px;top:34px">
    <span class="brand-dot"></span>
    <div class="brand-name" style="font-size:7.5px;width:80px">Fjellbrinken Tannregulering</div>
  </div>
  <div class="card-person"><strong>Stian Haugvik</strong><br>Kjeveortoped</div>
  <div class="footer-address" style="right:10px;bottom:8px;text-align:right">Myrbakkvegen 128, 5912 BERGEN<br>Telefon 55 83 17 62</div>
</section>

<!-- Business card, back -->
<section class="sheet card card-back">
  <svg style="position:absolute;left:0;top:0" width="60" height="96" viewBox="0 0 60 96" aria-hidden="true">
    <path d="M0 0 L30 0 C10 30 12 66 44 96 L0 96 Z" fill="var(--blue)"/>
  </svg>
  <div class="brand" style="left:56px;top:26px">
    <span class="brand-dot"></span>
    <div class="brand-name" style="font-size:7.5px;width:84px">Fjellbrinken Tannregulering</div>
  </div>
  <div class="web-bar" style="bottom:12px">www.smilbrink.no</div>
</section>

<!-- Envelope, address side -->
<section class="sheet envelope-back">
  <div class="brand" style="left:22px;top:16px">
    <span class="brand-dot"></span>
    <div class="brand-name">Fjellbrinken Tannregulering<div class="brand-tag">Kjeveortoped Stian Haugvik</div></div>
  </div>
  <div class="recipient-lines"><span></span><span></span><span></span><span></span></div>
  <svg class="swoosh" width="110" height="60" viewBox="0 0 110 60" aria-hidden="true">
    <path d="M0 8 C10 42 46 56 110 60 L0 60 Z" fill="var(--blue)"/>
  </svg>
  <div class="footer-address" style="left:64px;bottom:14px">Myrbakkvegen 128 · Postboks 71 Kvernvika<br>5912 BERGEN · Telefon 55 83 17 62</div>
  <div class="web-bar" style="bottom:12px">www.smilbrink.no</div>
</section>

<!-- Envelope, flap side -->
<section class="sheet envelope-flap">
  <svg style="position:absolute;left:0;top:0" width="384" height="125" viewBox="0 0 384 125" aria-hidden="true">
    <path d="M0 0 L384 0 L384 6 C300 40 250 70 192 78 C134 70 84 40 0 6 Z" fill="var(--blue)"/>
    <path d="M0 6 C84 40 134 70 192 78 C250 70 300 40 384 6" fill="none" stroke="var(--blue-light)" stroke-width="2"/>
  </svg>
  <span class="flap-mark"></span>
</section>

</body>
</html>
```